Minaret Hub design fresh look and feel

Need to create a Minaret Hub which has half a couple of dozen pages, a login page will take you into the main information with about 6 categories, such as school, memberships, information, prayer times etc... we have 3 types of users... 1. User .. admin user 3. imam user

I have xd files available.
https://mocks.plarvio.com/view/e4f7a2d1-8b3c-4f6e-a9d2-71b5c3e8f046-2ac7/

Target Market(s)

Muslims

Font styles to use
Sans Serif

Requirements
Must have
• Great UI
Simple flow

```html
<!DOCTYPE html>
<html lang="en">
<head>
<meta charset="utf-8">
<title>Minaret Hub – App Screens</title>
<link rel="stylesheet" href="https://fonts.googleapis.com/css2?family=Inter:wght@400;500;600;700&display=swap">
<style>
:root{
  --bg:#f2fbef;
  --green:#7bb87c;
  --teal:#62b1bb;
  --grad:linear-gradient(90deg,#7bb87c,#62b1bb);
  --ink:#263238;
  --muted:#8b9396;
  --line:#e3e8e6;
  --white:#ffffff;
  --red:#f0403f;
}
*{box-sizing:border-box;margin:0;padding:0}
html,body{width:1200px;height:1200px;overflow:hidden}
body{background:var(--bg);font-family:"Inter",sans-serif;color:var(--ink);position:relative}
.screen{position:absolute;width:240px;height:518px;background:var(--white);border-radius:24px;overflow:hidden;box-shadow:0 2px 10px rgba(60,120,80,.12)}
.screen *{position:absolute}
.status-time{top:8px;left:32px;font-size:9px;font-weight:600}
.status-icons{top:10px;right:18px;width:30px;height:8px}
.bottom-nav{left:0;right:0;bottom:0;height:44px;background:var(--white);box-shadow:0 -2px 6px rgba(0,0,0,.05)}
.bottom-nav svg{top:12px;width:18px;height:18px}
.nav-underline{left:32px;bottom:8px;width:18px;height:2px;background:var(--teal);border-radius:1px}

/* home */
.city{left:13px;top:37px;font-size:12px;font-weight:600}
.country{left:13px;top:54px;font-size:8px;font-weight:500}
.date{left:13px;top:70px;font-size:5.5px;color:var(--muted)}
.bell{right:14px;top:40px;width:13px;height:14px}
.prayer-card{left:13px;top:89px;width:213px;height:80px;border-radius:7px;background:var(--grad);overflow:hidden}
.prayer-label{left:11px;top:8px;font-size:8px;color:#eef8ee}
.prayer-time{left:11px;top:20px;font-size:17px;font-weight:500;color:var(--white)}
.prayer-left{left:11px;top:44px;font-size:7.5px;color:#eef8ee}
.prayer-mute{left:11px;top:63px;width:12px;height:9px}
.prayer-view{left:75px;top:63px;font-size:7.5px;color:var(--white)}
.prayer-art{right:0;top:0;width:100px;height:80px;background:linear-gradient(180deg,rgba(255,255,255,.55),rgba(255,255,255,.25))}
.menu-item{width:80px;height:60px}
.menu-icon{left:22px;top:0;width:36px;height:34px;border-radius:6px;background:var(--white);box-shadow:0 1px 4px rgba(0,0,0,.15)}
.menu-icon svg{left:8px;top:7px;width:20px;height:20px}
.menu-label{left:0;width:80px;top:40px;font-size:6.5px;color:var(--muted);text-align:center;line-height:1.35}
.section-title{left:18px;top:327px;font-size:10px;font-weight:600}
.section-link{right:18px;top:330px;font-size:6.5px;color:var(--green)}
.news-card{left:13px;width:213px;height:80px;border-radius:7px;overflow:hidden}
.news-photo{inset:0;background:linear-gradient(100deg,#c98c4a,#8a5a32 45%,#3d3a4a)}
.news-title{left:12px;top:44px;font-size:7.5px;color:var(--white);font-weight:500}
.news-btn{left:12px;top:60px;padding:1px 8px;font-size:5px;color:var(--white);background:rgba(255,255,255,.35);border-radius:6px;position:absolute}
.news-photo-2{inset:0;background:linear-gradient(180deg,#7d94b8,#c9ccd4)}

/* splash */
.splash{background:linear-gradient(180deg,#7bb97a,#61b0bc)}
.brand{left:0;right:0;top:236px;text-align:center;font-size:24px;font-weight:700;color:var(--white)}
.brand-dot{left:108px;top:200px;width:24px;height:24px;border-radius:50%;background:var(--white)}

/* login */
.welcome{left:14px;top:47px;font-size:11px;font-weight:700}
.welcome-sub{left:14px;top:75px;width:168px;font-size:6.3px;color:#4a5457;line-height:1.3}
.field{left:14px;width:213px;height:30px;border:1px solid var(--line);border-radius:7px}
.field .field-icon{left:10px;top:8px;width:13px;height:13px}
.field-text{left:37px;top:9px;font-size:7.5px;color:var(--muted)}
.field .select-chevron{left:auto;right:11px;top:12px;width:9px;height:6px}
.remember-box{left:14px;top:207px;width:8px;height:8px;border:1px solid #c8cfcc;border-radius:2px}
.remember{left:29px;top:207px;font-size:6.3px;color:var(--muted)}
.forgot{right:13px;top:207px;font-size:6.3px;color:var(--muted)}
.btn{height:29px;border-radius:7px;background:var(--grad);color:var(--white);font-size:11px;font-weight:500;display:flex;align-items:center;justify-content:center;letter-spacing:.5px}
.or-line{top:292px;height:1px;width:75px;background:var(--line)}
.or-text{left:0;right:0;top:288px;text-align:center;font-size:6.3px;color:var(--muted)}
.social{top:309px;width:100px;height:35px;background:var(--white);box-shadow:0 1px 4px rgba(0,0,0,.08);border-radius:3px;display:flex;align-items:center;justify-content:center;font-size:8px;font-weight:600;color:var(--ink)}
.signup{left:0;right:0;top:364px;text-align:center;font-size:6.3px;color:var(--green)}

/* list screens */
.back{left:12px;top:38px;width:14px;height:12px}
.page-title{left:0;right:0;top:38px;text-align:center;font-size:11px;font-weight:700}
.round-btn{top:68px;width:16px;height:16px}
.person-card{left:12px;top:95px;width:213px;height:57px;background:var(--white);border-radius:6px;box-shadow:0 1px 6px rgba(0,0,0,.1)}
.avatar{left:12px;top:10px;width:35px;height:35px;border-radius:50%;background:radial-gradient(circle at 50% 40%,#9fb0ad,#3b4f57)}
.person-name{left:58px;top:11px;font-size:8.5px;color:#3b4447}
.person-meta{left:58px;top:27px;font-size:4.8px;color:var(--muted);line-height:1.45;white-space:pre}
.pill{height:17px;border-radius:5px;color:var(--white);font-size:6.3px;display:flex;align-items:center;justify-content:center}
.pill-green{background:linear-gradient(90deg,#7bb87c,#6ab5a8)}
.sheet{left:0;right:0;top:212px;bottom:0;background:var(--white);border-radius:10px 10px 0 0;box-shadow:0 -3px 10px rgba(0,0,0,.08)}
.sheet-title{left:13px;top:20px;font-size:11px;font-weight:600}
.sheet-close{right:13px;top:21px;width:13px;height:13px}
.sheet .field-text{left:11px}
.donation-photo{left:12px;width:52px;height:52px;border-radius:5px;background:linear-gradient(160deg,#5d6e78,#2e3338 60%,#8a8780)}
.donation-title{left:75px;font-size:8.5px;color:#3b4447}
.donation-amount{left:75px;font-size:6.3px;color:var(--muted)}
.donation-date{left:75px;font-size:5px;color:var(--muted)}
.divider{left:12px;width:213px;height:1px;background:var(--line)}
.pill-red{background:var(--red)}
</style>
</head>
<body>

<!-- Home -->
<section class="screen" style="left:151px;top:53px">
  <span class="status-time">9:41</span>
  <svg class="status-icons" viewBox="0 0 30 8"><rect x="0" y="5" width="2" height="3" fill="#263238"/><rect x="3" y="3.5" width="2" height="4.5" fill="#263238"/><rect x="6" y="2" width="2" height="6" fill="#263238"/><path d="M11 4a5 5 0 0 1 7 0M12.5 5.5a3 3 0 0 1 4 0" stroke="#263238" fill="none" stroke-width="1.1"/><rect x="20" y="1.5" width="10" height="6" rx="1" fill="#263238"/></svg>
  <div class="city">London,</div>
  <div class="country">United Kingdom</div>
  <div class="date">Mon, 25 Jan 2021</div>
  <svg class="bell" viewBox="0 0 13 14"><path d="M6.5 1a4 4 0 0 1 4 4v4l1.5 2H1l1.5-2V5a4 4 0 0 1 4-4z" fill="#263238"/><circle cx="6.5" cy="12.5" r="1.5" fill="#263238"/></svg>
  <div class="prayer-card">
    <div class="prayer-art" role="img" aria-label="Illustration of a white mosque with minarets and crescent moons"></div>
    <div class="prayer-label">Next Prayer, Maghrib</div>
    <div class="prayer-time">18.25</div>
    <div class="prayer-left">(1 hour left until maghrib)</div>
    <svg class="prayer-mute" viewBox="0 0 12 9"><path d="M0 3h2l3-3v9L2 6H0z" fill="#fff"/><path d="M8 3l3 3M11 3L8 6" stroke="#fff" stroke-width="1"/></svg>
    <div class="prayer-view">View All</div>
  </div>

  <div class="menu-item" style="left:-3px;top:188px">
    <div class="menu-icon"><svg viewBox="0 0 20 20"><circle cx="10" cy="10" r="8" fill="none" stroke="#7bb87c" stroke-width="2.5"/><rect x="8" y="6" width="4" height="8" rx="1" fill="#62b1bb"/></svg></div>
    <div class="menu-label">My Madrassa</div>
  </div>
  <div class="menu-item" style="left:82px;top:188px">
    <div class="menu-icon"><svg viewBox="0 0 20 20"><rect x="11" y="2" width="6" height="7" rx="1.5" fill="#7bb87c"/><path d="M2 11h4l5 2h5a2 2 0 0 1 0 4H6l-4-2z" fill="#62b1bb"/></svg></div>
    <div class="menu-label">My Donation</div>
  </div>
  <div class="menu-item" style="left:162px;top:188px">
    <div class="menu-icon"><svg viewBox="0 0 20 20"><rect x="3" y="2" width="14" height="16" rx="2" fill="#7bb87c"/><circle cx="10" cy="10" r="3.5" fill="#fff"/><circle cx="10" cy="10" r="1.5" fill="#62b1bb"/></svg></div>
    <div class="menu-label">Suggestion Box</div>
  </div>
  <div class="menu-item" style="left:37px;top:252px">
    <div class="menu-icon"><svg viewBox="0 0 20 20"><path d="M10 1l7 5v12H3V6z" fill="#7bb87c"/><circle cx="10" cy="10" r="3.5" fill="#fff"/></svg></div>
    <div class="menu-label">NCWA Committe<br>Members</div>
  </div>
  <div class="menu-item" style="left:125px;top:252px">
    <div class="menu-icon"><svg viewBox="0 0 20 20"><rect x="2" y="9" width="16" height="7" rx="1.5" fill="#62b1bb"/><rect x="7" y="4" width="6" height="6" rx="1" fill="#7bb87c"/><circle cx="6" cy="12" r="1.5" fill="#fff"/></svg></div>
    <div class="menu-label">My Invites (2)</div>
  </div>

  <div class="section-title">Announcements</div>
  <div class="section-link">View All</div>
  <div class="news-card" style="top:353px">
    <div class="news-photo" role="img" aria-label="Photo of a man reading the Quran inside a warmly lit mosque"></div>
    <div class="news-title">Ramadan Kareem 2021 Date</div>
    <div class="news-btn">View More</div>
  </div>
  <div class="news-card" style="top:444px">
    <div class="news-photo-2" role="img" aria-label="Photo of white mosque domes under a blue sky"></div>
  </div>

  <nav class="bottom-nav">
    <svg style="left:32px" viewBox="0 0 18 18"><path d="M9 1l8 7v9h-6v-5H7v5H1V8z" fill="#7bb87c"/></svg>
    <svg style="left:111px" viewBox="0 0 18 18"><circle cx="9" cy="9" r="6" fill="none" stroke="#7bb87c" stroke-width="4" stroke-dasharray="2.5 2.2"/><circle cx="9" cy="9" r="4.5" fill="#7bb87c"/><circle cx="9" cy="9" r="2" fill="#fff"/></svg>
    <svg style="left:189px" viewBox="0 0 18 18"><circle cx="9" cy="5" r="4" fill="#62b1bb"/><path d="M1 17a8 6 0 0 1 16 0z" fill="#62b1bb"/></svg>
    <span class="nav-underline"></span>
  </nav>
</section>

<!-- Splash -->
<section class="screen splash" style="left:481px;top:53px">
  <span class="brand-dot"></span>
  <div class="brand">Minaret Hub</div>
</section>

<!-- Login -->
<section class="screen" style="left:810px;top:53px">
  <span class="status-time">9:41</span>
  <svg class="status-icons" viewBox="0 0 30 8"><rect x="0" y="5" width="2" height="3" fill="#263238"/><rect x="3" y="3.5" width="2" height="4.5" fill="#263238"/><rect x="6" y="2" width="2" height="6" fill="#263238"/><path d="M11 4a5 5 0 0 1 7 0M12.5 5.5a3 3 0 0 1 4 0" stroke="#263238" fill="none" stroke-width="1.1"/><rect x="20" y="1.5" width="10" height="6" rx="1" fill="#263238"/></svg>
  <div class="welcome">WELCOME BACK,</div>
  <div class="welcome-sub">Hello, welcome back to our apps. Please sign in with your email and password</div>
  <div class="field" style="top:110px">
    <svg class="field-icon" viewBox="0 0 13 13"><circle cx="6.5" cy="3.5" r="3" fill="#7b8488"/><path d="M0.5 13a6 5 0 0 1 12 0z" fill="#7b8488"/></svg>
    <span class="field-text">Username or email</span>
  </div>
  <div class="field" style="top:157px">
    <svg class="field-icon" viewBox="0 0 13 13"><circle cx="8.5" cy="4.5" r="3.3" fill="none" stroke="#7b8488" stroke-width="1.1"/><path d="M6 7L1 12" stroke="#7b8488" stroke-width="1.2"/></svg>
    <span class="field-text">Password</span>
  </div>
  <span class="remember-box"></span>
  <span class="remember">Remember me</span>
  <span class="forgot">Forgot password ?</span>
  <div class="btn" style="left:14px;top:235px;width:213px">Login</div>
  <span class="or-line" style="left:14px"></span>
  <span class="or-line" style="right:13px"></span>
  <div class="or-text">Or login with</div>
  <div class="social" style="left:14px">Searchly</div>
  <div class="social" style="left:126px">Friendbook</div>
  <div class="signup">Don't have any account? Sign up here.</div>
</section>

<!-- My Madrassa -->
<section class="screen" style="left:154px;top:635px">
  <span class="status-time">9:41</span>
  <svg class="status-icons" viewBox="0 0 30 8"><rect x="0" y="5" width="2" height="3" fill="#263238"/><rect x="3" y="3.5" width="2" height="4.5" fill="#263238"/><rect x="6" y="2" width="2" height="6" fill="#263238"/><path d="M11 4a5 5 0 0 1 7 0M12.5 5.5a3 3 0 0 1 4 0" stroke="#263238" fill="none" stroke-width="1.1"/><rect x="20" y="1.5" width="10" height="6" rx="1" fill="#263238"/></svg>
  <svg class="back" viewBox="0 0 14 12"><path d="M13 6H2M6 1L1 6l5 5" stroke="#263238" stroke-width="1.3" fill="none"/></svg>
  <div class="page-title">MY MADRASSA</div>
  <svg class="round-btn" style="left:13px" viewBox="0 0 16 16"><circle cx="8" cy="8" r="8" fill="#7bb87c"/><path d="M8 4v8M4 8h8" stroke="#fff" stroke-width="1.5"/></svg>
  <svg class="round-btn" style="left:186px" viewBox="0 0 16 16"><circle cx="8" cy="8" r="8" fill="#6ab5a8"/><circle cx="8.5" cy="7.5" r="3" fill="none" stroke="#fff" stroke-width="1.3"/><path d="M6.3 9.7L4.5 11.5" stroke="#fff" stroke-width="1.3"/></svg>
  <svg class="round-btn" style="left:209px" viewBox="0 0 16 16"><circle cx="8" cy="8" r="8" fill="#7bb87c"/><path d="M4 5h8l-3 4v3l-2-1V9z" fill="none" stroke="#fff" stroke-width="1.1"/></svg>
  <div class="person-card">
    <div class="avatar" role="img" aria-label="Profile photo of the child"></div>
    <div class="person-name">Amir Hadi</div>
    <div class="person-meta">Age            : 7
Gender       : Male
Quran level : Basic</div>
    <div class="pill pill-green" style="left:137px;top:20px;width:64px">View Details</div>
  </div>
  <nav class="bottom-nav">
    <svg style="left:32px" viewBox="0 0 18 18"><path d="M9 1l8 7v9h-6v-5H7v5H1V8z" fill="#7bb87c"/></svg>
    <svg style="left:111px" viewBox="0 0 18 18"><circle cx="9" cy="9" r="6" fill="none" stroke="#7bb87c" stroke-width="4" stroke-dasharray="2.5 2.2"/><circle cx="9" cy="9" r="4.5" fill="#7bb87c"/><circle cx="9" cy="9" r="2" fill="#fff"/></svg>
    <svg style="left:189px" viewBox="0 0 18 18"><circle cx="9" cy="5" r="4" fill="#62b1bb"/><path d="M1 17a8 6 0 0 1 16 0z" fill="#62b1bb"/></svg>
    <span class="nav-underline"></span>
  </nav>
</section>

<!-- My Madrassa – Add Person -->
<section class="screen" style="left:474px;top:630px">
  <span class="status-time">9:41</span>
  <svg class="status-icons" viewBox="0 0 30 8"><rect x="0" y="5" width="2" height="3" fill="#263238"/><rect x="3" y="3.5" width="2" height="4.5" fill="#263238"/><rect x="6" y="2" width="2" height="6" fill="#263238"/><path d="M11 4a5 5 0 0 1 7 0M12.5 5.5a3 3 0 0 1 4 0" stroke="#263238" fill="none" stroke-width="1.1"/><rect x="20" y="1.5" width="10" height="6" rx="1" fill="#263238"/></svg>
  <svg class="back" viewBox="0 0 14 12"><path d="M13 6H2M6 1L1 6l5 5" stroke="#263238" stroke-width="1.3" fill="none"/></svg>
  <div class="page-title">MY MADRASSA</div>
  <svg class="round-btn" style="left:13px" viewBox="0 0 16 16"><circle cx="8" cy="8" r="8" fill="#7bb87c"/><path d="M8 4v8M4 8h8" stroke="#fff" stroke-width="1.5"/></svg>
  <svg class="round-btn" style="left:186px" viewBox="0 0 16 16"><circle cx="8" cy="8" r="8" fill="#6ab5a8"/><circle cx="8.5" cy="7.5" r="3" fill="none" stroke="#fff" stroke-width="1.3"/><path d="M6.3 9.7L4.5 11.5" stroke="#fff" stroke-width="1.3"/></svg>
  <svg class="round-btn" style="left:209px" viewBox="0 0 16 16"><circle cx="8" cy="8" r="8" fill="#7bb87c"/><path d="M4 5h8l-3 4v3l-2-1V9z" fill="none" stroke="#fff" stroke-width="1.1"/></svg>
  <div class="person-card">
    <div class="avatar" role="img" aria-label="Profile photo of the child"></div>
    <div class="person-name">Amir Hadi</div>
    <div class="person-meta">Age            : 7
Gender       : Male
Quran level : Basic</div>
    <div class="pill pill-green" style="left:137px;top:20px;width:64px">View Details</div>
  </div>
  <div class="sheet">
    <div class="sheet-title">Add Person</div>
    <svg class="sheet-close" viewBox="0 0 13 13"><circle cx="6.5" cy="6.5" r="6.5" fill="#263238"/><path d="M4.5 4.5l4 4M8.5 4.5l-4 4" stroke="#fff" stroke-width="1.2"/></svg>
    <div class="field" style="top:55px"><span class="field-text">Name</span></div>
    <div class="field" style="top:99px"><span class="field-text">Age</span></div>
    <div class="field" style="top:143px"><span class="field-text">Gender</span><svg class="select-chevron" viewBox="0 0 9 6"><path d="M1 1l3.5 3.5L8 1" stroke="#4a5457" stroke-width="1.2" fill="none"/></svg></div>
    <div class="field" style="top:187px"><span class="field-text">Quran reading level</span><svg class="select-chevron" viewBox="0 0 9 6"><path d="M1 1l3.5 3.5L8 1" stroke="#4a5457" stroke-width="1.2" fill="none"/></svg></div>
    <div class="btn" style="left:13px;top:250px;width:213px">Add Person</div>
  </div>
</section>

<!-- My Donation -->
<section class="screen" style="left:794px;top:635px">
  <span class="status-time">9:41</span>
  <svg class="status-icons" viewBox="0 0 30 8"><rect x="0" y="5" width="2" height="3" fill="#263238"/><rect x="3" y="3.5" width="2" height="4.5" fill="#263238"/><rect x="6" y="2" width="2" height="6" fill="#263238"/><path d="M11 4a5 5 0 0 1 7 0M12.5 5.5a3 3 0 0 1 4 0" stroke="#263238" fill="none" stroke-width="1.1"/><rect x="20" y="1.5" width="10" height="6" rx="1" fill="#263238"/></svg>
  <svg class="back" viewBox="0 0 14 12"><path d="M13 6H2M6 1L1 6l5 5" stroke="#263238" stroke-width="1.3" fill="none"/></svg>
  <div class="page-title">MY DONATION</div>
  <svg class="round-btn" style="left:13px" viewBox="0 0 16 16"><circle cx="8" cy="8" r="8" fill="#7bb87c"/><path d="M8 4v8M4 8h8" stroke="#fff" stroke-width="1.5"/></svg>
  <svg class="round-btn" style="left:186px" viewBox="0 0 16 16"><circle cx="8" cy="8" r="8" fill="#6ab5a8"/><circle cx="8.5" cy="7.5" r="3" fill="none" stroke="#fff" stroke-width="1.3"/><path d="M6.3 9.7L4.5 11.5" stroke="#fff" stroke-width="1.3"/></svg>
  <svg class="round-btn" style="left:209px" viewBox="0 0 16 16"><circle cx="8" cy="8" r="8" fill="#7bb87c"/><path d="M4 5h8l-3 4v3l-2-1V9z" fill="none" stroke="#fff" stroke-width="1.1"/></svg>

  <div class="donation-photo" style="top:103px" role="img" aria-label="Photo of a burnt forest after a wildfire"></div>
  <div class="donation-title" style="top:112px">Forest Fires</div>
  <div class="donation-amount" style="top:125px">$150.00</div>
  <div class="donation-date" style="top:138px">21 December 2020</div>
  <div class="pill pill-green" style="left:161px;top:119px;width:64px">Success</div>
  <span class="divider" style="top:163px"></span>

  <div class="donation-photo" style="top:175px" role="img" aria-label="Photo of a burnt forest after a wildfire"></div>
  <div class="donation-title" style="top:185px">Forest Fires</div>
  <div class="donation-amount" style="top:198px">$15.00</div>
  <div class="donation-date" style="top:211px">21 December 2020</div>
  <div class="pill pill-red" style="left:161px;top:192px;width:64px">Declined</div>
  <span class="divider" style="top:236px"></span>

  <nav class="bottom-nav">
    <svg style="left:32px" viewBox="0 0 18 18"><path d="M9 1l8 7v9h-6v-5H7v5H1V8z" fill="#7bb87c"/></svg>
    <svg style="left:111px" viewBox="0 0 18 18"><circle cx="9" cy="9" r="6" fill="none" stroke="#7bb87c" stroke-width="4" stroke-dasharray="2.5 2.2"/><circle cx="9" cy="9" r="4.5" fill="#7bb87c"/><circle cx="9" cy="9" r="2" fill="#fff"/></svg>
    <svg style="left:189px" viewBox="0 0 18 18"><circle cx="9" cy="5" r="4" fill="#62b1bb"/><path d="M1 17a8 6 0 0 1 16 0z" fill="#62b1bb"/></svg>
    <span class="nav-underline"></span>
  </nav>
</section>

</body>
</html>
```